Simple elegant business card

General card for a fin and television director.
Just want name, email, phone and address.

Target Market(s)

Prospective employers

Industry/Entity Type

Business

Requirements
Must have
• As above
Nice to have
• Logo but not necessary.
Should not have
• Not too colourful or funky.
• Simplicity and elegance the way to go.

```html
<!DOCTYPE html>
<html lang="en">
<head>
<meta charset="utf-8">
<title>Nora Hale — Business Cards</title>
<link rel="stylesheet" href="https://fonts.googleapis.com/css2?family=Josefin+Slab:wght@400;600&family=Didact+Gothic&display=swap">
<style>
  :root {
    --ink: #000000;
    --flame: #ff5b37;
    --backdrop: #ececec;
  }
  * { box-sizing: border-box; margin: 0; padding: 0; }
  html, body {
    width: 1200px;
    height: 900px;
    overflow: hidden;
    background: var(--backdrop);
  }
  .card-pair {
    position: relative;
    width: 1200px;
    height: 900px;
  }
  .card {
    position: absolute;
    top: 45px;
    width: 490px;
    height: 810px;
    display: flex;
    flex-direction: column;
    align-items: center;
  }
  .card--dark { left: 100px; background: var(--ink); color: var(--flame); }
  .card--bright { left: 610px; background: var(--flame); color: var(--ink); }
  .card__emblem {
    margin-top: 110px;
    width: 160px;
    height: 160px;
    border-radius: 4px;
  }
  .card--dark .card__emblem { background: var(--flame); }
  .card--bright .card__emblem { background: var(--ink); }
  .card__name {
    margin-top: 12px;
    font-family: "Josefin Slab", serif;
    font-weight: 600;
    font-size: 96px;
    line-height: 84px;
    text-align: center;
    letter-spacing: 1px;
  }
  .card__contact {
    margin-top: auto;
    margin-bottom: 55px;
    font-family: "Didact Gothic", sans-serif;
    font-style: normal;
    font-size: 26px;
    line-height: 38px;
    text-align: center;
    letter-spacing: 0.5px;
  }
</style>
</head>
<body>
  <main class="card-pair">
    <section class="card card--dark">
      <div class="card__emblem" role="img" aria-label="Personal emblem area"></div>
      <h1 class="card__name">Nora<br>Hale</h1>
      <address class="card__contact">
        norahale@mail.com<br>+1 310 555 0142
      </address>
    </section>
    <section class="card card--bright">
      <div class="card__emblem" role="img" aria-label="Personal emblem area"></div>
      <h2 class="card__name">Nora<br>Hale</h2>
      <address class="card__contact">
        norahale@mail.com<br>+1 310 555 0142
      </address>
    </section>
  </main>
</body>
</html>
```